依頼詳細
ラックに並べられた時に見えるよう(雑誌のように)タイトルは上部にお願いします。写真を大きめに使ってください。美しい音で心に深くしみわたるような演奏にしたいと思っています。やさしく透明感のあるイメージでお願いします。
記載項目
森川沙織ピアノリサイタル
2014年11月8日(土)/開演18:00(開場17:30)
ソラノ心斎橋音楽サロン゛Brise”(大阪駅前第3ビル1F)
入場料(全自由席)前売:3000円 当日3500円 *未就学児の入場はごご遠慮くださいチケット販売 t* ティーナビ(サンデイストア Sunaターミナル)
お問い合わせ ソラノ心斎橋 大阪市北区曽根崎4丁目7番2(大阪駅前第3ビル1F)Tel. 06-6921-4057 , http://saorimori-piano.example/
後援 浪華音楽学院同窓会《響友会》、近畿鍵盤文化協会/
Program (原語表記のものを添付させていただきました)
モーツァルト/ソナタ第10番ハ長調 K.330
ラヴェル/ソナチネ
ラヴェル/「鏡」より 道化師の朝の歌
シューマン/交響的練習曲Op.13
Profile (添付させていただきました)
サイズ
A4
ページ数
片面
希望イメージ
シンプル 複雑
単色 カラフル
暗い 明るい
日常 高級
遊び心 厳粛
未来的 伝統的
女性的 男性的
希望する色
設定なし
納品ファイル
• イラストレーター形式 (.ai)
• フォトショップ形式 (.psd)
補足説明
写真を3枚添付していますが、どれか1枚を選んで使ってください。写真はイメージに合うようにカットしたり加工してくださって結構です。プログラムも添付しましたが、原語表記なしの日本語表記のみでも結構です。ナチュラルなイメージが希望です。
写真をもう一度添付してみました。
たびたび申し訳ありません。
プロフィール、並びに プログラムのファイルも添付できていなかったようなので、そちらももう一度添付します。
よろしくお願いいたします。
数々のご提案ありがとうございます。
みなさんとてもステキなのですが、私の好みを補足させていただきます。

顔以外のスペースが文字で埋まってしまうのは好きではありません。
「間」というのか、「抜け感」というのでしょうか…適度なスペースがほしいです。
音楽も「音と音のあいだに音楽が存在する」ものです。
こんな写真で申し訳ありませんが、ぜひアーティストとしてのセンス、インスピレーションを発揮してください☆よろしくお願いいたします。
■ 選んだ理由

私が表現したい音のイメージと合っているように思いました。
光のキラキラとしたようなものが入っていて、それが音のキラキラに通じるように思ったのと、透明感が感じられ、また柔らかい雰囲気もあると思います。
それなのに、チラシを見たときの印象が強いので、この提案に決めました。

■ 提案者全員のお礼・コメント

たくさんのご提案ありがとうございました。みなさんとてもステキなので、当選&次点を選ぶのが失礼なくらいでした。自分で考えるようなものとは全く違って、さすがプロのお仕事だなぁと思いました。多くのワガママを聞き入れてくださり、本当にありがとうございました。またお願いしたいと思います。感謝申し上げます。

```html
<!DOCTYPE html>
<html lang="ja">
<head>
<meta charset="utf-8">
<title>森川沙織 ピアノリサイタル</title>
<link href="https://fonts.googleapis.com/css2?family=Oswald:wght@200;300&family=Shippori+Mincho:wght@400;500&family=Great+Vibes&family=Noto+Sans+JP:wght@300;400;500&display=swap" rel="stylesheet">
<style>
:root{
  --paper:#fbf9f6;
  --ink:#4a4542;
  --soft:#8a837f;
  --title:#9a9490;
  --gold:#b89a5a;
  --accent:#c0392b;
  --photo-top:#d9d1c8;
  --photo-mid:#cdb9ae;
  --photo-low:#a86a72;
}
*{margin:0;padding:0;box-sizing:border-box}
html,body{width:849px;height:1200px;overflow:hidden;background:var(--paper)}
.flyer{position:relative;width:849px;height:1200px;overflow:hidden;
  background:linear-gradient(180deg,#ffffff 0%,var(--paper) 55%,#f4f0ea 100%);
  font-family:"Noto Sans JP",sans-serif;color:var(--ink)}
.portrait{position:absolute;left:0;top:108px;width:470px;height:780px;
  background:linear-gradient(180deg,var(--photo-top) 0%,var(--photo-mid) 55%,var(--photo-low) 100%);
  -webkit-mask-image:linear-gradient(90deg,#000 72%,transparent 100%);
  mask-image:linear-gradient(90deg,#000 72%,transparent 100%)}
.title{position:absolute;left:18px;top:14px;font-family:"Oswald",sans-serif;font-weight:200;
  font-size:112px;letter-spacing:5px;line-height:1;color:var(--title);white-space:nowrap}
.name{position:absolute;left:528px;top:106px;font-family:"Shippori Mincho",serif;font-size:62px;
  letter-spacing:6px;color:var(--soft);line-height:1}
.event{position:absolute;left:440px;top:198px;width:395px}
.date{font-family:"Shippori Mincho",serif;font-size:38px;color:var(--ink);letter-spacing:1px}
.date small{font-size:26px}
.time{margin-top:12px;font-size:19px;font-weight:500;letter-spacing:1px}
.venue{margin-top:8px;font-size:14px;line-height:1.5}
.venue .note{font-size:11px;color:var(--soft)}
.price{margin-top:8px;font-size:15px;display:flex;align-items:center;gap:10px}
.price .tag{background:var(--accent);color:#fff;font-size:12px;padding:2px 6px}
.sales{margin-top:6px;font-size:12px}
.sales .label{background:var(--ink);color:#fff;font-size:11px;padding:1px 5px;margin-right:6px}
.heading{font-family:"Great Vibes",cursive;color:var(--gold);font-size:54px;line-height:1}
.program{position:absolute;left:440px;top:412px;width:395px}
.program ol{list-style:none;margin-top:12px;margin-left:24px}
.program li{margin-bottom:14px;font-size:17px;line-height:1.35}
.program li .orig{display:block;font-size:11px;color:var(--soft);font-family:"Shippori Mincho",serif}
.profile{position:absolute;left:14px;top:892px;width:580px}
.profile .head{display:flex;align-items:baseline;gap:20px}
.profile .heading{font-size:48px}
.profile .who{font-family:"Shippori Mincho",serif;font-size:20px}
.profile .who span{font-family:"Great Vibes",cursive;color:var(--gold);font-size:20px;margin-left:8px}
.profile p{margin-top:8px;font-size:11px;line-height:1.8;color:var(--ink);text-align:justify}
.contact{position:absolute;left:617px;top:952px;width:220px;font-size:12px;line-height:1.7;color:var(--ink)}
.contact .block{margin-bottom:10px}
.contact .url{margin-top:8px;color:var(--soft);font-size:11px}
</style>
</head>
<body>
<main class="flyer">
  <div class="portrait" role="img" aria-label="ピアニストのポートレート写真"></div>
  <h1 class="title">PIANO RECITAL</h1>
  <div class="name">森川沙織</div>

  <section class="event">
    <div class="date">2014年11月8日<small>(土)</small></div>
    <div class="time">18:00開演 ｜ 17:30開場</div>
    <div class="venue">ソラノ心斎橋音楽サロン゛Brise”<br><span class="note">＊未就学児の入場はご遠慮ください</span></div>
    <div class="price"><span class="tag">全席自由</span>前売3000円｜当日3500円</div>
    <div class="sales"><span class="label">販売</span>t*（ティーナビ）サンデイストア Sunaターミナル</div>
  </section>

  <section class="program">
    <div class="heading">Program</div>
    <ol>
      <li>モーツァルト　ソナタ第10番ハ長調 K.330<span class="orig">W.A.Mozart: Sonate No.10 C-dur K.330</span></li>
      <li>ラヴェル　ソナチネ<span class="orig">M.Ravel: Sonatine</span></li>
      <li>ラヴェル　「鏡」より 道化師の朝の歌<span class="orig">M.Ravel: Miroirs – Alborada del gracioso</span></li>
      <li>シューマン　交響的練習曲 Op.13<span class="orig">R.Schumann: Sinfonische Etüden Op.13</span></li>
    </ol>
  </section>

  <section class="profile">
    <div class="head"><div class="heading">Profile</div><div class="who">森川沙織<span>Saori Morikawa</span></div></div>
    <p>兵庫県生まれ。4歳よりピアノを始める。浪華音楽学院ピアノ科卒業。在学中より室内楽や伴奏の分野で研鑽を積み、卒業後は欧州にて研修を受ける。帰国後は関西を中心にソロリサイタルや室内楽の演奏会に出演し、繊細で透明感のある音色が高い評価を得ている。これまでに各地の音楽祭に招かれ、地域のサロンコンサートや学校公演にも力を注ぐ。現在、後進の指導にあたりながら演奏活動を続けている。浪華音楽学院同窓会《響友会》会員、近畿鍵盤文化協会会員。</p>
  </section>

  <section class="contact">
    <div class="block">お問い合わせ<br>ソラノ心斎橋<br>大阪市北区曽根崎4丁目7番2<br>（浪速中央第5ビル1F）<br>Tel. 06-6921-4057</div>
    <div class="block">後援<br>浪華音楽学院同窓会《響友会》<br>近畿鍵盤文化協会</div>
    <div class="url">http://saorimori-piano.example/</div>
  </section>
</main>
</body>
</html>
```